Business card design needed

We need a business card design for a new micro business based in Melbourne (Australia). Our main service is cleaning and fixing Vertical Blinds as a cheaper alternative than buying new blinds. A smaller part of the business is fitting affordable & temporary alternatives to double glazed windows both for noise abatement and climate control and reduction in energy costs.
We could be dealing with commercial as well as residential customers so we need a quality look. The design needs to reflect our core business of vertical blinds cleaning & maintenance.

Target Market(s)

Not sure yet. These Business Cards are going to be used to test the market

Industry/Entity Type

Residential

Contact Information for Business Card

Teloria Brinkhaus. Vertical Blinds Cleaning, Maintenance & Temporary Window Insulation Solutions. Ph: 03 9274 5163. Mob: 0497 362 514.

```html
<!DOCTYPE html>
<html lang="en">
<head>
<meta charset="utf-8">
<title>Teloria Brinkhaus – Business Card</title>
<link rel="stylesheet" href="https://fonts.googleapis.com/css2?family=Anton&family=Roboto+Condensed:ital,wght@1,700;1,800&display=swap">
<style>
  :root {
    --page-bg: #e6e6e6;
    --card-cream: #ece9dc;
    --card-cream-light: #f4f2e8;
    --card-shade: #8c8470;
    --card-frame: #dcd8c6;
    --brand-green: #2f6f57;
    --ink-dark: #1c1c1a;
  }
  * { margin: 0; padding: 0; box-sizing: border-box; }
  html, body {
    width: 1200px;
    height: 900px;
    overflow: hidden;
    background: var(--page-bg);
  }
  .business-card {
    position: absolute;
    left: 150px;
    top: 175px;
    width: 900px;
    height: 550px;
    border-radius: 22px;
    overflow: hidden;
    box-shadow: 0 10px 30px rgba(0,0,0,0.18);
  }
  .card-photo {
    position: absolute;
    inset: 0;
    background:
      linear-gradient(90deg, var(--card-shade) 0%, #a39a80 20%, var(--card-frame) 24%, var(--card-cream) 30%, var(--card-cream-light) 100%);
  }
  .card-content {
    position: absolute;
    inset: 0;
  }
  .owner-name {
    position: absolute;
    left: 310px;
    top: 155px;
    width: 540px;
    text-align: center;
    font-family: "Anton", "Impact", sans-serif;
    font-size: 60px;
    line-height: 1;
    letter-spacing: 0.5px;
    color: var(--brand-green);
    transform: skewX(-6deg);
    text-shadow: 1px 1px 0 var(--ink-dark);
  }
  .service-line {
    position: absolute;
    left: 300px;
    top: 245px;
    width: 560px;
    text-align: center;
    font-family: "Roboto Condensed", "Arial Narrow", sans-serif;
    font-style: italic;
    font-weight: 800;
    font-size: 25px;
    line-height: 38px;
    color: var(--ink-dark);
  }
  .contact-row {
    position: absolute;
    left: 320px;
    top: 420px;
    display: flex;
    gap: 90px;
    align-items: center;
  }
  .contact-item {
    display: flex;
    align-items: center;
    gap: 16px;
    font-family: "Roboto Condensed", "Arial Narrow", sans-serif;
    font-style: italic;
    font-weight: 700;
    font-size: 27px;
    color: var(--ink-dark);
  }
  .contact-icon { fill: var(--brand-green); }
</style>
</head>
<body>
  <div class="business-card">
    <div class="card-photo" role="img" aria-label="Photo of cream horizontal window blinds beside a textured curtain, with a glass bowl of succulents on the sill"></div>
    <div class="card-content">
      <h1 class="owner-name">TELORIA BRINKHAUS</h1>
      <p class="service-line">Vertical Cleaning, Maintenance and<br>Temporary Insulation Solutions for Windows</p>
      <div class="contact-row">
        <div class="contact-item phone">
          <svg class="contact-icon" width="40" height="40" viewBox="0 0 40 40" aria-hidden="true">
            <path d="M4 12c0-4 6-7 16-7s16 3 16 7v3h-8v-3c-2-1-5-1.5-8-1.5s-6 .5-8 1.5v3H4z"/>
            <path d="M12 16h16l6 18H6z"/>
            <circle cx="20" cy="25" r="4" fill="#ece9dc"/>
          </svg>
          <span>03 9274 5163</span>
        </div>
        <div class="contact-item mobile">
          <svg class="contact-icon" width="26" height="40" viewBox="0 0 26 40" aria-hidden="true">
            <rect x="2" y="1" width="22" height="38" rx="3"/>
            <rect x="6" y="5" width="14" height="11" fill="#ece9dc"/>
            <g fill="#ece9dc">
              <rect x="6" y="20" width="3" height="3"/><rect x="11.5" y="20" width="3" height="3"/><rect x="17" y="20" width="3" height="3"/>
              <rect x="6" y="26" width="3" height="3"/><rect x="11.5" y="26" width="3" height="3"/><rect x="17" y="26" width="3" height="3"/>
              <rect x="6" y="32" width="3" height="3"/><rect x="11.5" y="32" width="3" height="3"/><rect x="17" y="32" width="3" height="3"/>
            </g>
          </svg>
          <span>0497 362 514</span>
        </div>
      </div>
    </div>
  </div>
</body>
</html>
```